a residential painting contractor I need a 6x9 postcard made

I already have a logo, I'm trying to offer my services to people. you can put that there's a 250$ discount for first time customers. include my License number #4627381 as well as the services I offer, interior and exterior painting, pressure washing, cabinet painting, epoxy floors, wood staining, decks, fences and much more. I'm licensed bonded and insured as well.

Target Market(s)

residential consumers (homeowners)

Industry/Entity Type

Painting contractor

Requirements
Must have
• postage stuff on the back I've linked some pictures top right please, my license number, what I do, phone number (555)317-0846 email velbrushworks7@mailzo.net, front and back of postcard
Nice to have
• well lit house in the background, maybe little circles of people doing some of the services I offer

```html
<!DOCTYPE html>
<html lang="en">
<head>
<meta charset="utf-8">
<title>Velbrush Works – Postcard Front and Back</title>
<link rel="stylesheet" href="https://fonts.googleapis.com/css2?family=Bebas+Neue&family=Montserrat:wght@400;500;600;700;800&display=swap">
<style>
  :root {
    --ink: #262626;
    --white: #ffffff;
    --accent: #f5e81c;
    --paper: #f1eadc;
    --paper-edge: #ddd0b6;
    --sky-top: #9fc0dc;
    --sky-mid: #d9e6f0;
    --wall: #ecd7c4;
    --roof: #b4654a;
    --lawn: #6f8a4e;
    --stage: #ececec;
    --rule: #555555;
  }
  * { box-sizing: border-box; margin: 0; padding: 0; }
  html, body { width: 800px; height: 1200px; overflow: hidden; }
  body {
    background: var(--stage);
    font-family: "Montserrat", sans-serif;
    color: var(--ink);
    position: relative;
  }
  .postcard {
    position: absolute;
    left: 30px;
    width: 740px;
    height: 493px;
    overflow: hidden;
    box-shadow: 0 3px 10px rgba(0,0,0,.18);
  }
  .postcard--front { top: 55px; background: var(--white); }
  .postcard--back {
    top: 620px;
    background: radial-gradient(ellipse at 40% 45%, var(--paper) 55%, var(--paper-edge) 100%);
  }
  .display { font-family: "Bebas Neue", sans-serif; font-weight: 400; line-height: 1; }

  /* ---------- front ---------- */
  .house-photo {
    position: absolute; left: 280px; top: 0; width: 460px; height: 420px;
    background:
      linear-gradient(90deg, var(--white) 0%, rgba(255,255,255,0) 30%),
      linear-gradient(180deg, var(--sky-top) 0%, var(--sky-mid) 28%, var(--wall) 55%, var(--roof) 72%, var(--wall) 82%, var(--lawn) 100%);
  }
  .brand {
    position: absolute; left: 45px; top: 70px;
    display: flex; align-items: center; gap: 10px;
  }
  .brand__dot { width: 22px; height: 22px; border-radius: 50%; background: var(--ink); }
  .brand__name { font-family: "Bebas Neue", sans-serif; font-size: 40px; color: var(--ink); line-height: 1; }
  .headline { position: absolute; left: 33px; top: 214px; }
  .headline__line { display: block; color: var(--ink); }
  .headline__line--1 { font-size: 31px; letter-spacing: .2px; }
  .headline__line--2 { font-size: 39px; margin-top: 2px; }
  .headline__line--3 {
    display: inline-block; font-size: 46px; color: var(--white);
    background: var(--ink); padding: 3px 5px 0; margin-top: 2px;
  }
  .front-tagline {
    position: absolute; left: 33px; top: 350px; width: 240px;
    font-size: 10.5px; font-weight: 600; line-height: 1.3;
  }
  .discount-badge {
    position: absolute; width: 150px; height: 142px; border-radius: 50%;
    background: var(--ink); color: var(--white);
    display: flex; flex-direction: column; align-items: center; justify-content: center;
    text-align: center;
  }
  .discount-badge--front { left: 393px; top: 48px; transform: rotate(-6deg); }
  .discount-badge__amount { font-family: "Bebas Neue", sans-serif; font-size: 58px; color: var(--accent); line-height: .9; }
  .discount-badge__label {
    font-weight: 800; font-size: 15px; letter-spacing: .3px;
    border-bottom: 1px solid var(--white); padding-bottom: 1px;
  }
  .discount-badge__note { font-size: 12px; line-height: 1.05; margin-top: 3px; }
  .contact-band { position: absolute; left: 0; bottom: 0; width: 740px; height: 95px; }
  .contact-band__edge { position: absolute; left: 0; top: 0; }
  .contact-band__phone {
    position: absolute; left: 33px; top: 32px; font-size: 48px; color: var(--white);
  }
  .contact-band__divider {
    position: absolute; left: 438px; top: 36px; width: 1px; height: 40px; background: var(--white);
  }
  .contact-band__details {
    position: absolute; left: 466px; top: 33px; color: var(--white);
    font-size: 15.5px; font-weight: 500; line-height: 25px;
  }
  .contact-row { display: flex; align-items: center; gap: 9px; white-space: nowrap; }
  .contact-row svg { flex: none; }

  /* ---------- back ---------- */
  .what-we-do { position: absolute; left: 25px; top: 38px; width: 192px; }
  .section-title { font-size: 28px; }
  .what-we-do__text {
    margin-top: 6px; font-size: 10.6px; line-height: 1.42; text-align: justify;
  }
  .discount-badge--back { left: 228px; top: 66px; width: 120px; height: 114px; transform: rotate(-4deg); }
  .discount-badge--back .discount-badge__amount { font-size: 44px; }
  .discount-badge--back .discount-badge__label { font-size: 11px; }
  .discount-badge--back .discount-badge__note { font-size: 9px; }
  .postal-box {
    position: absolute; border: 1px solid var(--ink); background: var(--white);
    font-family: Arial, sans-serif; font-weight: 700; color: var(--ink);
  }
  .postal-box--customer { left: 410px; top: 32px; width: 178px; height: 44px; font-size: 12px; padding: 6px 12px; line-height: 1.3; }
  .postal-box--permit { left: 616px; top: 32px; width: 98px; height: 76px; font-size: 10.5px; text-align: center; padding-top: 3px; line-height: 1.33; }
  .postal-box--permit .permit-paid { font-size: 12px; }
  .services {
    position: absolute; left: 0; top: 205px; width: 372px; height: 162px;
    background: var(--ink); color: var(--white); padding: 16px 25px 0;
  }
  .services__columns { display: flex; margin-top: 10px; }
  .services__list { list-style: none; font-size: 11px; }
  .services__list li { display: flex; align-items: center; gap: 5px; height: 25px; white-space: nowrap; }
  .services__list--left { width: 196px; padding-right: 10px; border-right: 1px solid var(--white); }
  .services__list--right { padding-left: 21px; }
  .address-lines { position: absolute; left: 410px; top: 270px; width: 304px; }
  .address-lines span { display: block; height: 30px; border-bottom: 1px solid var(--rule); }
  .back-contact { position: absolute; left: 25px; top: 378px; }
  .back-contact__phone { font-size: 41px; }
  .back-contact__row { font-size: 20px; font-weight: 500; margin-top: 6px; gap: 12px; }
</style>
</head>
<body>

<section class="postcard postcard--front" aria-label="Postcard front">
  <div class="house-photo" role="img" aria-label="Photo of a large well-lit two-storey house with terracotta roofs under a blue sky"></div>

  <div class="brand">
    <span class="brand__dot"></span>
    <span class="brand__name">VELBRUSH WORKS</span>
  </div>

  <h1 class="headline display">
    <span class="headline__line headline__line--1">YOUR PAINTING CONTRACTOR</span>
    <span class="headline__line headline__line--2">SHOULD BE AVAILABLE</span>
    <span class="headline__line headline__line--3">FOR EMERGENCIES</span>
  </h1>
  <p class="front-tagline">Lorem Ipsum is simply dummy text of the printing and typesetting industry.</p>

  <div class="discount-badge discount-badge--front">
    <span class="discount-badge__amount">250$</span>
    <span class="discount-badge__label">DISCOUNT</span>
    <span class="discount-badge__note">for first time<br>customers</span>
  </div>

  <div class="contact-band">
    <svg class="contact-band__edge" width="740" height="95" viewBox="0 0 740 95" aria-hidden="true">
      <path fill="#262626" d="M0 10 L40 8 L70 12 L110 6 L150 11 L200 7 L240 10 L290 5 L330 9 L380 6 L420 10 L470 4 L520 9 L570 6 L610 10 L660 5 L700 9 L740 6 L740 95 L0 95 Z"/>
    </svg>
    <div class="contact-band__phone display">CALL US: (555)317-0846</div>
    <div class="contact-band__divider"></div>
    <div class="contact-band__details">
      <div class="contact-row">
        <svg width="16" height="12" viewBox="0 0 16 12" aria-hidden="true"><rect x="0.5" y="0.5" width="15" height="11" fill="#fff"/><path d="M1 1 L8 7 L15 1" stroke="#262626" stroke-width="1.4" fill="none"/></svg>
        <span>velbrushworks7@mailzo.net</span>
      </div>
      <div class="contact-row">
        <svg width="16" height="16" viewBox="0 0 16 16" aria-hidden="true"><rect x="2" y="1" width="12" height="14" rx="1" fill="#fff"/><path d="M4.5 5h7M4.5 8h7M4.5 11h4" stroke="#262626" stroke-width="1.3"/></svg>
        <span>License number #4627381</span>
      </div>
    </div>
  </div>
</section>

<section class="postcard postcard--back" aria-label="Postcard back">
  <div class="what-we-do">
    <h2 class="section-title display">WHAT WE DO</h2>
    <p class="what-we-do__text">Lorem Ipsum is simply dummy text of the printing and typesetting industry. Lorem Ipsum has been the industry's standard dummy text ever since the 1500s, when an unknown printer took a galley of type and scrambled it to make a type specimen book.</p>
  </div>

  <div class="discount-badge discount-badge--back">
    <span class="discount-badge__amount">250$</span>
    <span class="discount-badge__label">DISCOUNT</span>
    <span class="discount-badge__note">for first time<br>customers</span>
  </div>

  <div class="postal-box postal-box--customer">LOCAL POSTAL<br>CUSTOMER</div>
  <div class="postal-box postal-box--permit">PRSRT STD<br>ECRWSS<br>U.S.POSTAGE<br><span class="permit-paid">PAID</span><br>EDDM Retail</div>

  <div class="services">
    <h2 class="section-title display">OUR SERVICES</h2>
    <div class="services__columns">
      <ul class="services__list services__list--left">
        <li><svg width="10" height="10" viewBox="0 0 10 10" aria-hidden="true"><circle cx="5" cy="5" r="5" fill="#fff"/><path d="M2.6 5.2 L4.3 6.8 L7.4 3.4" stroke="#262626" stroke-width="1.4" fill="none"/></svg>Interior and exterior painting</li>
        <li><svg width="10" height="10" viewBox="0 0 10 10" aria-hidden="true"><circle cx="5" cy="5" r="5" fill="#fff"/><path d="M2.6 5.2 L4.3 6.8 L7.4 3.4" stroke="#262626" stroke-width="1.4" fill="none"/></svg>Pressure washing</li>
        <li><svg width="10" height="10" viewBox="0 0 10 10" aria-hidden="true"><circle cx="5" cy="5" r="5" fill="#fff"/><path d="M2.6 5.2 L4.3 6.8 L7.4 3.4" stroke="#262626" stroke-width="1.4" fill="none"/></svg>Cabinet painting</li>
        <li><svg width="10" height="10" viewBox="0 0 10 10" aria-hidden="true"><circle cx="5" cy="5" r="5" fill="#fff"/><path d="M2.6 5.2 L4.3 6.8 L7.4 3.4" stroke="#262626" stroke-width="1.4" fill="none"/></svg>Epoxy floors</li>
      </ul>
      <ul class="services__list services__list--right">
        <li><svg width="10" height="10" viewBox="0 0 10 10" aria-hidden="true"><circle cx="5" cy="5" r="5" fill="#fff"/><path d="M2.6 5.2 L4.3 6.8 L7.4 3.4" stroke="#262626" stroke-width="1.4" fill="none"/></svg>Wood staining</li>
        <li><svg width="10" height="10" viewBox="0 0 10 10" aria-hidden="true"><circle cx="5" cy="5" r="5" fill="#fff"/><path d="M2.6 5.2 L4.3 6.8 L7.4 3.4" stroke="#262626" stroke-width="1.4" fill="none"/></svg>Decks</li>
        <li><svg width="10" height="10" viewBox="0 0 10 10" aria-hidden="true"><circle cx="5" cy="5" r="5" fill="#fff"/><path d="M2.6 5.2 L4.3 6.8 L7.4 3.4" stroke="#262626" stroke-width="1.4" fill="none"/></svg>Fences and</li>
        <li><svg width="10" height="10" viewBox="0 0 10 10" aria-hidden="true"><circle cx="5" cy="5" r="5" fill="#fff"/><path d="M2.6 5.2 L4.3 6.8 L7.4 3.4" stroke="#262626" stroke-width="1.4" fill="none"/></svg>Much more</li>
      </ul>
    </div>
  </div>

  <div class="address-lines" aria-hidden="true"><span></span><span></span><span></span><span></span></div>

  <div class="back-contact">
    <div class="back-contact__phone display">CALL US: (555)317-0846</div>
    <div class="contact-row back-contact__row">
      <svg width="19" height="14" viewBox="0 0 16 12" aria-hidden="true"><rect x="0.5" y="0.5" width="15" height="11" fill="#262626"/><path d="M1 1 L8 7 L15 1" stroke="#f1eadc" stroke-width="1.4" fill="none"/></svg>
      <span>velbrushworks7@mailzo.net</span>
    </div>
    <div class="contact-row back-contact__row">
      <svg width="19" height="19" viewBox="0 0 16 16" aria-hidden="true"><rect x="2" y="1" width="12" height="14" rx="1" fill="#262626"/><path d="M4.5 5h7M4.5 8h7M4.5 11h4" stroke="#f1eadc" stroke-width="1.3"/></svg>
      <span>License number #4627381</span>
    </div>
  </div>
</section>

</body>
</html>
```